Brisk Motion Flyer - Physiotherapy company

I am looking for a two-sided flyer (4"x8") that can be easily posted on cork boards or displayed as needed to provide information about my business. I would like to use the colors found in my logo (see attached) along with white and black. Please have a look at my website for ideas of how I would like the color schemes etc (www.briskmotion.example). I would like it to follow the same style as my website.<br/><br/>FRONT SIDE<br/>I am hoping to have the name of our business "Brisk Motion" with our slogan "Boreal Physiotherapy - Rehab and Recovery Above the Line (degrees symbol)" underneath. Somewhere above or around this I would like my logo (see attached). <br/><br/>Below that I would like a title "Services Provided" and then listed: <br/>Mobile Services<br/>Clinic<br/>Telehealth<br/><br/>Below that, I would like another title "Treatments Offered" and then listed: <br/>Hands-on manual therapy<br/>Intramuscular Stimulation (IMS)<br/>Acupuncture<br/>Athletic taping<br/>Injury/condition education<br/>Supervised exercise<br/><br/>Below that I would like "Contact Us":<br/>Brisk Motion<br/>www.BriskMotion.example<br/>Book online through https://briskmotion.bookerly.example/<br/>physio@briskmotion.example<br/>867-555-0148<br/>Direct Billing offered for most extended health providers<br/>(friendwall, Pictagram logo, movetrak logo (see attached) on bottom maybe in corner or centered)<br/><br/>BACK SIDE<br/><br/>I would like the logo on there once again maybe. Then I would like these three information sections one on top of the other spaced out appropriately.<br/><br/>Image (needling image) (see attached)<br/>Title: Mobile Physiotherapy<br/>The information below title: If you want to keep moving and need some help, but your current condition makes it difficult or unsafe to travel to and from a clinic to see a physiotherapist, that’s where we come in. We make it easy by offering a mobile service that provides exceptional one-on-one physiotherapy assessment and treatment in the comfort of your own home. There is a small fee to access mobile services. <br/><br/>Image (Hands on knee image) (see attached)<br/>Title: Clinic<br/>The information below title: If you have an injury that is causing you pain or restricting you from doing the activities that you want to do then physiotherapy can help. A traditional approach to physiotherapy where you come to our clinic and we provide one to one education and hands on therapy. <br/><br/>Image (computer, tablet etc) (see attached)<br/>Title: Telehealth<br/>The information below title: If you live outside of Whitehorse or just want easy access to a physiotherapist from the comfort of your home, then Telehealth is for you. Telehealth involves meeting with your physiotherapist using real-time technology, similar to ViewTalk. Brisk Motion utilizes Movetrakker for exercise prescription, pain tracking and telehealth. Through Movetrakker or it’s Kinetapp you can discuss your treatment plan, diagnoses, exercises, daily activities or any other questions you may have directly with a physiotherapist.<br/><br/><br/><br/>

Industry/Entity Type

Healthcare

Colors

Designer to choose colors to be used in the design.

Requirements
Must have
• Follow the same colors and schemes of my website (www.briskmotion.example)
• Keep it clean and concise
Nice to have
• Images might not fit because I don't want it too cluttered.
Should not have
• Too busy

```html
<!DOCTYPE html>
<html lang="en">
<head>
<meta charset="utf-8">
<title>Brisk Motion Flyer</title>
<link href="https://fonts.googleapis.com/css2?family=EB+Garamond:wght@400;700&family=Montserrat:wght@500;700&family=Source+Sans+3:wght@400&family=Roboto+Condensed:wght@400&display=swap" rel="stylesheet">
<style>
:root{
  --stage:#616161;
  --navy:#2b4a7a;
  --navy-dark:#213a63;
  --green:#0f5a45;
  --teal:#35b89b;
  --ink:#222;
  --paper:#fff;
  --sky-top:#ffffff;
  --sky-bottom:#c9d9ef;
}
*{box-sizing:border-box;margin:0;padding:0}
html,body{width:1200px;height:1200px;overflow:hidden;background:var(--stage)}
.flyer{position:absolute;top:189px;width:417px;height:833px;background:var(--paper);overflow:hidden;font-family:"Source Sans 3",sans-serif;color:var(--ink)}
.flyer--front{left:110px;background:linear-gradient(180deg,var(--sky-top) 0%,var(--sky-bottom) 40%,var(--paper) 62%)}
.flyer--back{left:607px}
.abs{position:absolute}
.center{left:0;right:0;text-align:center}

/* front header */
.brand-mark{top:52px;font-family:"EB Garamond",serif;font-weight:700;color:var(--green);font-size:26px;letter-spacing:3px;line-height:1}
.brand-mark span{display:inline-block;width:9px;height:9px;background:var(--navy);margin-right:8px;vertical-align:middle}
.brand-sub{top:84px;font-family:"EB Garamond",serif;font-weight:700;color:var(--navy);font-size:13px;letter-spacing:6px}
.title{top:158px;font-family:"EB Garamond",serif;font-weight:700;color:var(--navy);font-size:38px;line-height:1;letter-spacing:.5px}
.slogan-1{top:220px;font-family:"EB Garamond",serif;font-weight:700;color:var(--green);font-size:23px;line-height:1}
.slogan-2{top:248px;font-family:"EB Garamond",serif;color:var(--navy);font-size:23px;line-height:1}
.hero{top:300px;left:0;width:417px;height:216px;background:linear-gradient(180deg,#b7c8e3 0%,#7d93b7 35%,#4d5f80 62%,#3d3530 85%,#5a3f30 100%)}

/* services */
.services{top:540px;left:24px;width:367px;height:90px;border:1.5px solid var(--green);border-radius:6px}
.services-tag{top:531px;left:114px;width:189px;height:20px;background:var(--green);color:#fff;font-family:"Montserrat",sans-serif;font-weight:700;font-size:12.5px;letter-spacing:.6px;text-align:center;line-height:20px;clip-path:polygon(6% 0,94% 0,100% 50%,94% 100%,6% 100%,0 50%)}
.service{top:556px;width:110px;text-align:center}
.service svg{display:block;margin:0 auto}
.service p{margin-top:6px;font-family:"Montserrat",sans-serif;font-weight:500;font-size:13px;color:var(--ink)}

/* treatments */
.section-title{font-family:"Montserrat",sans-serif;font-weight:700;color:var(--navy);font-size:14px;letter-spacing:.6px}
.treat-title{top:649px}
.treat-list{list-style:none;font-size:13.5px;line-height:20.5px}
.treat-list li{padding-left:12px;position:relative}
.treat-list li::before{content:"";position:absolute;left:0;top:8px;width:6px;height:6px;border-radius:50%;background:var(--green)}

/* front footer */
.footer{left:0;width:417px;background:var(--navy);border-top:2px solid var(--green)}
.flyer--front .footer{top:750px;height:83px}
.book-pill{top:740px;left:57px;width:303px;height:21px;border-radius:11px;background:var(--green);border:1px solid #fff;color:#fff;font-size:11px;text-align:center;line-height:19px}
.contact-row{top:772px;left:26px;right:20px;display:flex;justify-content:space-between;color:#fff;font-size:11px;align-items:center}
.contact-row svg{vertical-align:-1px;margin-right:4px}
.billing{top:798px;left:30px;width:238px;white-space:nowrap;color:#fff;font-family:"Roboto Condensed",sans-serif;font-size:10px;letter-spacing:-.1px}
.app-name{font-family:"Source Sans 3",sans-serif;color:var(--teal);font-size:15px}
.social{color:#fff;font-size:8.5px}
.front-apps{top:794px;right:14px;display:flex;gap:6px;align-items:center}
.front-apps .app-name{font-size:14px}
.front-apps .social{font-size:8px}

/* back */
.photo{left:26px;width:365px;height:105px;border:1px solid #98a9c4}
.photo--needle{top:26px;background:linear-gradient(90deg,#f4f4f4 0%,#e9dfd6 45%,#d8b59d 80%,#c99a7d 100%)}
.photo--knee{top:269px;background:linear-gradient(90deg,#6b6b6b 0%,#a0715a 25%,#3b3b3b 50%,#d9d6d2 100%)}
.photo--devices{top:481px;background:#d4d4d4}
.back-title{text-align:center;left:26px;width:365px}
.body-text{left:26px;width:365px;font-size:11.6px;line-height:14.8px;text-align:justify}
.flyer--back .footer{top:741px;height:92px}
.back-brand{top:770px;left:26px;width:70px;text-align:center;color:#fff;font-family:"EB Garamond",serif;font-weight:700;line-height:1}
.back-brand b{display:block;font-size:15px;letter-spacing:1.5px}
.back-brand i{display:block;font-style:normal;font-size:7px;letter-spacing:3px;margin-top:3px}
.back-contacts{top:762px;left:122px;color:#fff;font-size:12px;line-height:17.5px}
.back-contacts svg{vertical-align:-1px;margin-right:6px}
.back-apps{top:765px;right:26px;text-align:right}
.back-apps .social{display:block;font-size:9px;margin-bottom:6px}
.back-apps .app-name{font-size:17px}
</style>
</head>
<body>

<section class="flyer flyer--front" aria-label="Flyer front">
  <div class="abs center brand-mark"><span></span>BRISK MOTION</div>
  <div class="abs center brand-sub">PHYSIOTHERAPY</div>
  <h1 class="abs center title">BRISK MOTION</h1>
  <p class="abs center slogan-1">BOREAL PHYSIOTHERAPY</p>
  <p class="abs center slogan-2">Rehab and Recovery Above the Line°</p>
  <div class="abs hero" role="img" aria-label="Photo of two hikers climbing a rocky ridge with misty blue mountain ranges behind"></div>

  <div class="abs services"></div>
  <div class="abs services-tag">SERVICES PROVIDED</div>
  <div class="abs service" style="left:34px">
    <svg width="44" height="44" viewBox="0 0 44 44"><circle cx="22" cy="22" r="21" fill="var(--green)"/><circle cx="22" cy="22" r="18" fill="var(--navy)" stroke="#fff" stroke-width="1.5"/><path d="M14 28h16M16 28v-7l6-5 6 5v7" fill="none" stroke="#fff" stroke-width="1.5"/><rect x="20" y="22" width="4" height="6" fill="#fff"/></svg>
    <p>Mobile Services</p>
  </div>
  <div class="abs service" style="left:153px">
    <svg width="44" height="44" viewBox="0 0 44 44"><circle cx="22" cy="22" r="21" fill="var(--green)"/><circle cx="22" cy="22" r="18" fill="var(--navy)" stroke="#fff" stroke-width="1.5"/><rect x="14" y="17" width="16" height="13" fill="none" stroke="#fff" stroke-width="1.5"/><path d="M22 10v6M19 13h6" stroke="#fff" stroke-width="1.5"/><path d="M17 21h2M21 21h2M25 21h2M17 25h2M25 25h2" stroke="#fff" stroke-width="1.5"/></svg>
    <p>Clinic</p>
  </div>
  <div class="abs service" style="left:271px">
    <svg width="44" height="44" viewBox="0 0 44 44"><circle cx="22" cy="22" r="21" fill="var(--green)"/><circle cx="22" cy="22" r="18" fill="var(--navy)" stroke="#fff" stroke-width="1.5"/><rect x="12" y="14" width="20" height="13" rx="1.5" fill="none" stroke="#fff" stroke-width="1.5"/><path d="M18 31h8M22 27v4M15 21h4l2-3 2 6 2-3h4" fill="none" stroke="#fff" stroke-width="1.3"/></svg>
    <p>Telehealth</p>
  </div>

  <h2 class="abs center section-title treat-title">TREATMENTS OFFERED</h2>
  <ul class="abs treat-list" style="top:667px;left:33px">
    <li>Hands-on manual therapy</li>
    <li>Intramuscular Stimulation(IMS)</li>
    <li>Injury/condition education</li>
  </ul>
  <ul class="abs treat-list" style="top:667px;left:260px">
    <li>Acupuncture</li>
    <li>Athletic taping</li>
    <li>Supervised exercise</li>
  </ul>

  <div class="abs footer"></div>
  <div class="abs book-pill">Book online through https://briskmotion.bookerly.example/</div>
  <div class="abs contact-row">
    <span><svg width="9" height="9" viewBox="0 0 10 10"><path d="M2 1l2 2-1 1.5c.7 1.3 1.3 1.9 2.5 2.5L7 6l2 2-1.2 1.3C4.5 9 1 5.5.8 2.2z" fill="var(--teal)"/></svg>867-555-0148</span>
    <span><svg width="10" height="8" viewBox="0 0 10 8"><rect x=".5" y=".5" width="9" height="7" fill="none" stroke="var(--teal)"/><path d="M.5 .5L5 4.5 9.5 .5" fill="none" stroke="var(--teal)"/></svg>physio@briskmotion.example</span>
    <span><svg width="9" height="9" viewBox="0 0 10 10"><circle cx="5" cy="5" r="4.3" fill="none" stroke="var(--teal)"/><path d="M.7 5h8.6M5 .7c-2 2.5-2 6 0 8.6M5 .7c2 2.5 2 6 0 8.6" fill="none" stroke="var(--teal)" stroke-width=".8"/></svg>www.BriskMotion.example</span>
  </div>
  <p class="abs billing">Direct Billing offered for most extended health providers</p>
  <div class="abs front-apps">
    <span class="app-name">Kinetapp</span>
    <span class="social">friendwall</span>
    <span class="social">Pictagram</span>
  </div>
</section>

<section class="flyer flyer--back" aria-label="Flyer back">
  <div class="abs photo photo--needle" role="img" aria-label="Close-up photo of hands placing acupuncture needles in a shoulder"></div>
  <h2 class="abs section-title back-title" style="top:140px">MOBILE PHYSIOTHERAPY</h2>
  <p class="abs body-text" style="top:157px">If you want to keep moving and need some help, but your current condition makes it difficult or unsafe to travel to and from a clinic to see a physiotherapist, that’s where we come in. We make it easy by offering a mobile service that provides exceptional one-on-one physiotherapy assessment and treatment in the comfort of your own home. There is a small fee to access mobile services.</p>

  <div class="abs photo photo--knee" role="img" aria-label="Photo of a physiotherapist's hands working on a patient's bent knee"></div>
  <h2 class="abs section-title back-title" style="top:380px">CLINIC</h2>
  <p class="abs body-text" style="top:397px">If you have an injury that is causing you pain or restricting you from doing the activities that you want to do then physiotherapy can help. A traditional approach to physiotherapy where you come to our clinic and we provide one to one education and hands on therapy.</p>

  <div class="abs photo photo--devices" role="img" aria-label="Laptop, tablet and phone showing an exercise and video call app"></div>
  <h2 class="abs section-title back-title" style="top:593px">TELEHEALTH</h2>
  <p class="abs body-text" style="top:610px">If you live outside of Whitehorse or just want easy access to a physiotherapist from the comfort of your home, then Telehealth is for you. Telehealth involves meeting with your physiotherapist using real-time technology, similar to ViewTalk. Brisk Motion utilizes Movetrakker for exercise prescription, pain tracking and telehealth. Through Movetrakker or it’s Kinetapp you can discuss your treatment plan, diagnoses, exercises, daily activities or any other questions you may have directly with a physiotherapist.</p>

  <div class="abs footer"></div>
  <div class="abs back-brand"><b>BRISK</b><b>MOTION</b><i>PHYSIO</i></div>
  <div class="abs back-contacts">
    <div><svg width="10" height="10" viewBox="0 0 10 10"><path d="M2 1l2 2-1 1.5c.7 1.3 1.3 1.9 2.5 2.5L7 6l2 2-1.2 1.3C4.5 9 1 5.5.8 2.2z" fill="var(--teal)"/></svg>867-555-0148</div>
    <div><svg width="10" height="8" viewBox="0 0 10 8"><rect x=".5" y=".5" width="9" height="7" fill="none" stroke="var(--teal)"/><path d="M.5 .5L5 4.5 9.5 .5" fill="none" stroke="var(--teal)"/></svg>physio@briskmotion.example</div>
    <div><svg width="10" height="10" viewBox="0 0 10 10"><circle cx="5" cy="5" r="4.3" fill="none" stroke="var(--teal)"/><path d="M.7 5h8.6M5 .7c-2 2.5-2 6 0 8.6M5 .7c2 2.5 2 6 0 8.6" fill="none" stroke="var(--teal)" stroke-width=".8"/></svg>www.BriskMotion.example</div>
  </div>
  <div class="abs back-apps">
    <span class="social">friendwall · Pictagram</span>
    <span class="app-name">Kinetapp</span>
  </div>
</section>

</body>
</html>
```